Health software company called BRIGHT MERIDIAN, committed to innovation and technological excellence

The powerpoint presentation template is necessary, very necessary is elegant and modern with innovative images and the color palette attached. The presentation will be used for the business plan and investor presentations that we will use to raise funds. Please, recommend a modern typeface, as well as format to be able to use it and incorporate it as part of the company's brand guidelines. Great diversity of technological solutions
Updates

Very low attendance of designers for a high budget. Very few proposals and no capture my interest

Need extra days to review

Need extra days to review

Need extra days to review

Target Market(s)

managers, managers of public and private health centers, government states, investors

Industry/Entity Type

It Company

Font styles to use
Serif

Requirements
Must have
• The powerpoint presentation template is necessary, very necessary is elegant, minimalist and modern with innovative images and the color palette attached. it must be refined in demarcated style
Nice to have
• very nice, visually harmonic avoid saturation
Should not have
• NO dark colors NO dark colors NO dark colors NO dark colors NO dark colors

```html
<!DOCTYPE html>
<html lang="en">
<head>
<meta charset="utf-8">
<title>Bright Meridian — Title Slide</title>
<link rel="stylesheet" href="https://fonts.googleapis.com/css2?family=Ubuntu:wght@300;400&display=swap">
<style>
  :root {
    --sky-light: #f4f8fc;
    --sky-mid: #cfe2f1;
    --sky-deep: #9cc3e3;
    --scarf-blue: #3f9fdc;
    --brand-blue: #118fdc;
    --brand-blue-deep: #0a80cf;
    --brand-blue-soft: #2a9fe6;
    --edge-blue: #48aeea;
    --text-white: #ffffff;
  }

  html, body {
    margin: 0;
    padding: 0;
    width: 1200px;
    height: 900px;
    overflow: hidden;
    background: #ffffff;
  }

  .slide {
    position: relative;
    width: 1200px;
    height: 900px;
    overflow: hidden;
    font-family: "Ubuntu", "Helvetica Neue", Arial, sans-serif;
  }

  .hero-photo {
    position: absolute;
    inset: 0;
    background:
      radial-gradient(ellipse 420px 520px at 300px 600px, rgba(255,255,255,0.9), rgba(255,255,255,0) 70%),
      linear-gradient(200deg, var(--scarf-blue) 0%, rgba(63,159,220,0) 35%),
      linear-gradient(180deg, var(--sky-mid) 0%, var(--sky-light) 45%, var(--sky-deep) 100%);
  }

  .brand-panel {
    position: absolute;
    inset: 0;
    width: 1200px;
    height: 900px;
  }

  .title-block {
    position: absolute;
    left: 635px;
    top: 420px;
    color: var(--text-white);
  }

  .company-name {
    margin: 0;
    font-weight: 300;
    font-size: 58px;
    line-height: 1;
    letter-spacing: 0.5px;
    white-space: nowrap;
  }

  .tagline {
    margin: 14px 0 0 8px;
    font-weight: 300;
    font-size: 18px;
    line-height: 1;
    white-space: nowrap;
  }
</style>
</head>
<body>
  <main class="slide">
    <div class="hero-photo" role="img" aria-label="Photo of a smiling woman with arms outstretched holding a flowing blue scarf against a bright cloudy sky"></div>

    <svg class="brand-panel" viewBox="0 0 1200 900" aria-hidden="true">
      <defs>
        <radialGradient id="panelGlow" cx="0.6" cy="0.5" r="0.7">
          <stop offset="0" stop-color="var(--brand-blue-soft)"/>
          <stop offset="0.6" stop-color="var(--brand-blue)"/>
          <stop offset="1" stop-color="var(--brand-blue-deep)"/>
        </radialGradient>
      </defs>
      <polygon class="panel-edge" points="752,0 774,0 392,900 370,900" fill="var(--edge-blue)"/>
      <polygon class="panel-fill" points="772,0 1200,0 1200,900 390,900" fill="url(#panelGlow)"/>
    </svg>

    <header class="title-block">
      <h1 class="company-name">BRIGHT MERIDIAN</h1>
      <p class="tagline">committed to innovation and technological excellence</p>
    </header>
  </main>
</body>
</html>
```